Koala Hound & Critter Haulage

We need a new business card for a new business. We transport animals mainly dogs specialising in greyhounds travelling locally and interstate in air conditioned comfort. The design should incorporate the australian flag

Reason: just want to get the right design

```html
<!DOCTYPE html>
<html lang="en">
<head>
<meta charset="utf-8">
<title>Koala Hound &amp; Critter Haulage — Business Card</title>
<link href="https://fonts.googleapis.com/css2?family=Gelasio:wght@400&display=swap" rel="stylesheet">
<style>
  :root {
    --page-bg: #d9d9d9;
    --card-black: #0b0c0d;
    --card-black-soft: #1a1c1e;
    --brand-blue: #12489a;
    --divider-grey: #4b4d50;
    --text-light: #ffffff;
  }
  * { margin: 0; padding: 0; box-sizing: border-box; }
  html, body {
    width: 1200px;
    height: 985px;
    overflow: hidden;
    background: var(--page-bg);
    font-family: "Gelasio", Georgia, serif;
  }
  .stage {
    width: 1200px;
    height: 985px;
    display: flex;
    align-items: center;
    justify-content: center;
  }
  .business-card {
    position: relative;
    width: 840px;
    height: 480px;
    border-radius: 28px;
    overflow: hidden;
    background: var(--brand-blue);
    box-shadow: 0 12px 30px rgba(0,0,0,0.25);
  }
  .card-top {
    position: absolute;
    left: 0; top: 0;
    width: 100%;
    height: 200px;
    background: radial-gradient(ellipse at 40% 30%, var(--card-black-soft), var(--card-black) 70%);
  }
  .card-divider {
    position: absolute;
    left: 0; top: 200px;
    width: 100%;
    height: 8px;
    background: var(--divider-grey);
  }
  .brand {
    position: absolute;
    left: 150px;
    top: 150px;
    display: flex;
    align-items: center;
    gap: 12px;
  }
  .brand-mark {
    width: 22px;
    height: 22px;
    background: var(--brand-blue);
  }
  .brand-name {
    font-size: 30px;
    color: var(--brand-blue);
    line-height: 1;
    white-space: nowrap;
  }
  .holder-name {
    position: absolute;
    left: 60px;
    top: 236px;
    font-size: 28px;
    color: var(--text-light);
  }
  .contact-list {
    position: absolute;
    left: 540px;
    top: 340px;
    list-style: none;
    color: var(--text-light);
    font-size: 22px;
    line-height: 1.25;
  }
  .contact-list li {
    display: flex;
    align-items: center;
    gap: 8px;
  }
  .contact-icon {
    width: 18px;
    height: 18px;
    flex: none;
  }
  .contact-phone { font-size: 26px; }
</style>
</head>
<body>
  <main class="stage">
    <article class="business-card">
      <div class="card-top"></div>
      <div class="card-divider"></div>

      <div class="brand">
        <span class="brand-mark"></span>
        <span class="brand-name">Koala Hound &amp; Critter Haulage</span>
      </div>

      <p class="holder-name">Tom Hallett</p>

      <ul class="contact-list">
        <li class="contact-phone">
          <svg class="contact-icon" viewBox="0 0 18 18" aria-hidden="true">
            <rect x="0" y="0" width="18" height="18" rx="3" fill="#ffffff"/>
            <path d="M6 4 L8 4 L8.5 7 L7 8 Q8 10.5 10 11 L11 9.5 L14 10 L14 12 Q13.5 14 11 13.5 Q5.5 12 4.5 6.5 Q4.5 4.5 6 4 Z" fill="#12489a"/>
          </svg>
          0400 555 123
        </li>
        <li>
          <svg class="contact-icon" viewBox="0 0 18 18" aria-hidden="true" fill="none" stroke="#ffffff" stroke-width="1.2">
            <circle cx="9" cy="9" r="7.5"/>
            <ellipse cx="9" cy="9" rx="3.5" ry="7.5"/>
            <line x1="1.5" y1="9" x2="16.5" y2="9"/>
            <line x1="3" y1="5" x2="15" y2="5"/>
            <line x1="3" y1="13" x2="15" y2="13"/>
          </svg>
          TBA
        </li>
        <li>ABN 12345678901</li>
      </ul>
    </article>
  </main>
</body>
</html>
```